Vértice Solar needs the best stationery in the development business

We need a stationary design for a new company based in Porto, Portugal. We are a new property development management company specialized in downtown regeneration projects and adaptive use of old big textile factories.

We just have selected our new logo in a pixelbazaar competition and now we are searching for the best stationary design. We expect to receive proposals for:

Two sided business cards
A4 main letterhead
A4 simple text papper
A4 and A5 envelops
A4 single folder front page

information for the stationary project

company signature: FormaCrescimentoDireção (as in the logo files attached)

Business card information: 
Tomás Vieira Lobato FRICS
Managing Director

email: tomas@verticesolar-exemplo.pt
website: www.verticesolar-exemplo.pt

adress: 
R. das Camélias, 83 - 2º
4050-217 Porto

office number
+(351) 22 418 76 53
fax number
+(351) 22 418 76 59
mobile
+(351) 934 207 615

Target Market(s)

professional finantial fund managers and big property owners

Industry/Entity Type

Business

Requirements
Must have
• the company logo

Nice to have
• clear simple contemporary design is appreciated

```html
<!DOCTYPE html>
<html lang="pt">
<head>
<meta charset="utf-8">
<title>Vértice Solar — Business Cards</title>
<link rel="stylesheet" href="https://fonts.googleapis.com/css2?family=Open+Sans:wght@400;600;700;800&display=swap">
<style>
  :root {
    --page-bg: #ecebe8;
    --card-white: #ffffff;
    --card-grey: #a8a9ab;
    --brand-blue: #2c62ad;
    --ink: #4a4a4a;
    --ink-soft: #6b6b6b;
    --on-grey: #ffffff;
    --shadow: rgba(0, 0, 0, 0.18);
  }
  * { box-sizing: border-box; margin: 0; padding: 0; }
  html, body { width: 1200px; height: 720px; overflow: hidden; }
  body {
    background: var(--page-bg);
    font-family: "Open Sans", Arial, sans-serif;
    display: flex;
    align-items: center;
    justify-content: center;
    gap: 48px;
  }
  .card {
    width: 540px;
    height: 330px;
    position: relative;
    box-shadow: 0 6px 18px var(--shadow);
  }
  /* Front */
  .card--front { background: var(--card-white); }
  .front-brand {
    position: absolute;
    left: 34px; top: 0; bottom: 0;
    width: 250px;
    display: flex; flex-direction: column; justify-content: center; align-items: flex-start;
    padding-top: 30px;
  }
  .brand-mark {
    width: 44px; height: 44px; border-radius: 50%;
    background: var(--brand-blue);
    margin: 0 0 10px 60px;
  }
  .brand-name {
    font-weight: 800;
    font-size: 36px;
    letter-spacing: -1px;
    line-height: 1;
    color: var(--brand-blue);
    white-space: nowrap;
  }
  .brand-tagline {
    margin-top: 6px;
    font-weight: 700;
    font-size: 12.5px;
    color: var(--brand-blue);
    letter-spacing: 0.1px;
  }
  .front-divider {
    position: absolute;
    left: 300px; top: 40px;
    width: 2px; height: 150px;
    background: var(--brand-blue);
  }
  .front-contact {
    position: absolute;
    left: 316px; top: 40px;
    color: var(--ink);
    font-size: 11.5px;
    line-height: 1.5;
  }
  .contact-name { font-weight: 700; color: var(--brand-blue); font-size: 12.5px; }
  .contact-role { color: var(--ink-soft); font-size: 10.5px; margin-bottom: 10px; }
  .contact-list { list-style: none; }
  .contact-list li { display: flex; align-items: center; gap: 6px; }
  .contact-list svg { width: 10px; height: 10px; fill: var(--brand-blue); flex: none; }
  .contact-address { margin-top: 12px; }

  /* Back */
  .card--back {
    background: var(--card-grey);
    color: var(--on-grey);
    display: flex; flex-direction: column; align-items: center; justify-content: center;
  }
  .card--back .brand-mark {
    background: var(--on-grey);
    width: 56px; height: 56px;
    margin: 0 0 12px 0;
  }
  .card--back .brand-name { color: var(--on-grey); font-size: 48px; }
  .card--back .brand-tagline { color: var(--on-grey); font-size: 15px; margin-top: 8px; }
  .back-website {
    margin-top: 30px;
    font-size: 15px;
    letter-spacing: 1.5px;
  }
</style>
</head>
<body>
  <section class="card card--front" aria-label="Business card front">
    <div class="front-brand">
      <span class="brand-mark" aria-hidden="true"></span>
      <span class="brand-name">Vértice Solar</span>
      <span class="brand-tagline">FormaCrescimentoDireção</span>
    </div>
    <div class="front-divider" aria-hidden="true"></div>
    <div class="front-contact">
      <p class="contact-name">Tomás Vieira Lobato FRICS</p>
      <p class="contact-role">Managing Director</p>
      <ul class="contact-list">
        <li><svg viewBox="0 0 10 10"><path d="M2 0.5 L4 0.5 L4.5 3 L3.3 4 Q4.5 6 6 6.7 L7 5.5 L9.5 6 L9.5 8 Q9.5 9.5 8 9.5 Q1 8.5 0.5 2 Q0.5 0.5 2 0.5Z"/></svg>+(351) 22 418 76 53</li>
        <li><svg viewBox="0 0 10 10"><rect x="2" y="0.5" width="6" height="3"/><rect x="0.5" y="4" width="9" height="5" rx="1"/></svg>+(351) 22 418 76 59</li>
        <li><svg viewBox="0 0 10 10"><rect x="2.5" y="0.5" width="5" height="9" rx="1"/></svg>+(351) 934 207 615</li>
        <li><svg viewBox="0 0 10 10"><path d="M0.5 2 H9.5 V8.5 H0.5Z M0.5 2 L5 5.5 L9.5 2" /></svg>tomas@verticesolar-exemplo.pt</li>
        <li><svg viewBox="0 0 10 10"><circle cx="5" cy="5" r="4.5"/></svg>www.verticesolar-exemplo.pt</li>
      </ul>
      <p class="contact-address">R. das Camélias, 83 - 2º<br>4050-217 Porto</p>
    </div>
  </section>

  <section class="card card--back" aria-label="Business card back">
    <span class="brand-mark" aria-hidden="true"></span>
    <span class="brand-name">Vértice Solar</span>
    <span class="brand-tagline">FormaCrescimentoDireção</span>
    <span class="back-website">www.verticesolar-exemplo.pt</span>
  </section>
</body>
</html>
```